Bright Meadow Counseling Business Card design with a visually interesting use of Space

I need business cards that are luxurious and give a peaceful, calm vibe. I also had some letterhead designed, and i like the look of it also, it's attached with the logo design for reference/ ideas but feel free to be creative.

Target Market(s)

High end luxurious client who needs counseling

Industry/Entity Type

Marriage and Family Therapy

Contact Information for Business Card

Mira Kowalczyk MS LMFT/ or Toby Hallett address 4150 Larkin Suite 600

Font styles to use
Sans Serif

Colors
0054AA
0677BA
7BADD7
CADEEF
E8F1F8
0094D4
00A9DD
6FCCEA
C7EBF8
E9F6FB
A7469A
B969AE
D3A5CF
EDDBEB
F8F0F9
6B429C
8869AF
B7A5CE
E3DAEB
F3F0F8

Requirements
Must have
• Logo and color scheme but be simple modern and luxurious
Nice to have
• I'd like to incorporate some elelmets from the logo and letterhead into a simple modern card

```html
<!DOCTYPE html>
<html lang="en">
<head>
<meta charset="utf-8">
<title>Bright Meadow Counseling – Business Card</title>
<link rel="stylesheet" href="https://fonts.googleapis.com/css2?family=Montserrat:wght@300;400;700&display=swap">
<style>
  :root {
    --backdrop: #2b2b2d;
    --card: #ffffff;
    --ink: #1d1d1f;
    --teal: #2a7f88;
    --teal-soft: #72bfb7;
    --sky: #7badd7;
    --blue: #4a6fb8;
    --purple: #8869af;
    --magenta: #a7469a;
  }
  * { box-sizing: border-box; margin: 0; padding: 0; }
  html, body {
    width: 1200px; height: 1024px; overflow: hidden;
    background: var(--backdrop);
    font-family: "Montserrat", sans-serif;
    color: var(--ink);
  }
  .canvas { position: relative; width: 1200px; height: 1024px; }
  .card {
    position: absolute; left: 230px; width: 740px; height: 423px;
    background: var(--card);
    box-shadow: 0 14px 30px rgba(0,0,0,.55);
    overflow: hidden;
  }
  .card--front { top: 58px; }
  .card--back { top: 543px; }

  .brand-field {
    position: absolute; top: 0;
    background: linear-gradient(105deg, var(--sky) 0%, var(--blue) 30%, var(--purple) 60%, var(--magenta) 100%);
    -webkit-mask-image: radial-gradient(ellipse 60% 75% at 60% 25%, #000 55%, transparent 100%);
            mask-image: radial-gradient(ellipse 60% 75% at 60% 25%, #000 55%, transparent 100%);
  }
  .card--front .brand-field { left: 250px; width: 490px; height: 270px; opacity: .8; }
  .card--back .brand-field { left: 430px; width: 310px; height: 190px; opacity: .12; }

  .wordmark {
    position: absolute; display: flex; align-items: center; gap: 14px;
    font-weight: 300; color: var(--ink); white-space: nowrap;
  }
  .wordmark__dot { border-radius: 50%; background: var(--teal-soft); flex: none; }
  .card--front .wordmark { left: 140px; top: 318px; font-size: 36px; }
  .card--front .wordmark__dot { width: 22px; height: 22px; }
  .card--back .wordmark { left: 300px; top: 350px; font-size: 26px; }
  .card--back .wordmark__dot { width: 16px; height: 16px; }

  .person { position: absolute; left: 60px; top: 200px; }
  .person__name { font-weight: 700; font-size: 28px; color: var(--teal); letter-spacing: .02em; line-height: 1.1; }
  .person__role { font-weight: 400; font-size: 17px; letter-spacing: .06em; margin-top: 2px; }

  .contact {
    position: absolute; right: 50px; top: 120px;
    text-align: right; font-style: normal; font-size: 14px; font-weight: 400; line-height: 1.5;
  }
  .contact__address { margin-bottom: 12px; }
  .contact__line { display: flex; justify-content: flex-end; align-items: center; gap: 8px; }
  .contact__line svg { width: 13px; height: 13px; fill: var(--teal); flex: none; }
  .contact__email { margin-top: 10px; }
  .contact__web { margin-top: 10px; font-weight: 700; color: var(--teal); letter-spacing: .06em; font-size: 16px; }
</style>
</head>
<body>
<main class="canvas">
  <section class="card card--front">
    <div class="brand-field" role="img" aria-label="Brand decoration area in sky blue, violet and magenta tones"></div>
    <p class="wordmark"><span class="wordmark__name">Bright Meadow Counseling</span><span class="wordmark__dot"></span></p>
  </section>

  <section class="card card--back">
    <div class="brand-field" role="img" aria-label="Faint brand decoration area in soft violet and pink tones"></div>

    <div class="person">
      <p class="person__name">CORIN WELLS</p>
      <p class="person__role">MANAGER</p>
    </div>

    <address class="contact">
      <p class="contact__address">2214 Willowbend Road<br>Fairhaven Oregon 97120</p>
      <p class="contact__line">541-208-7734
        <svg viewBox="0 0 24 24" aria-hidden="true"><path d="M6.6 10.8a15 15 0 0 0 6.6 6.6l2.2-2.2c.3-.3.7-.4 1-.2 1.1.4 2.3.6 3.6.6.6 0 1 .4 1 1V20c0 .6-.4 1-1 1A17 17 0 0 1 3 4c0-.6.4-1 1-1h3.5c.6 0 1 .4 1 1 0 1.3.2 2.5.6 3.6.1.3 0 .7-.2 1z"/></svg>
      </p>
      <p class="contact__line">541-208-7735
        <svg viewBox="0 0 24 24" aria-hidden="true"><path d="M6 2h10l2 2v5H6zM3 10h18v9h-3v3H6v-3H3zm5 6v4h8v-4z"/></svg>
      </p>
      <p class="contact__line contact__email">hello@brightmeadow.com
        <svg viewBox="0 0 24 24" aria-hidden="true"><path d="M2 5h20v14H2zm2 2v.5l8 5 8-5V7z"/></svg>
      </p>
      <p class="contact__web">www.brightmeadow.com</p>
    </address>

    <p class="wordmark"><span class="wordmark__name">Bright Meadow Counseling</span><span class="wordmark__dot"></span></p>
  </section>
</main>
</body>
</html>
```